we are in the infrastructure business ( road construction ) and I need a billboard that I placed it at every project to illustrate that we worked there . We have the logo , I attached it , I just need an interesting design of the billboard.
The company s name is : Vela Structura - I attached how to be written !
I don't need to write road construction business on it

Requirements
Must have
• Study the design of the logo I attached ( the sign with " TBK " is just an example !!
Nice to have
• the romanian flag but made into a special form ( I attached an Idea )

```html
<!DOCTYPE html>
<html lang="en">
<head>
<meta charset="utf-8">
<title>Vela Structura – Project Billboard</title>
<link rel="stylesheet" href="https://fonts.googleapis.com/css2?family=Montserrat:wght@600&display=swap">
<style>
  :root {
    --flag-blue: #002b7f;
    --flag-yellow: #fcd116;
    --flag-red: #ce1126;
    --ink: #1f222d;
    --paper: #ffffff;
    --haze: #c9ccc9;
  }
  * { margin: 0; padding: 0; box-sizing: border-box; }
  html, body {
    width: 1200px;
    height: 581px;
    overflow: hidden;
    background: var(--paper);
  }
  .billboard {
    position: relative;
    width: 1200px;
    height: 581px;
    background: var(--paper);
    overflow: hidden;
  }
  .flag-band {
    display: flex;
    height: 29px;
  }
  .flag-band span { flex: 1; }
  .flag-band .blue { background: var(--flag-blue); }
  .flag-band .yellow { background: var(--flag-yellow); }
  .flag-band .red { background: var(--flag-red); }

  .company-name {
    font-family: "Montserrat", sans-serif;
    font-weight: 600;
    color: var(--ink);
    text-transform: uppercase;
    line-height: 1;
  }
  .company-name .name-top {
    position: absolute;
    left: 84px;
    top: 100px;
    font-size: 206px;
    letter-spacing: 30px;
  }
  .company-name .name-bottom {
    position: absolute;
    right: 80px;
    top: 282px;
    font-size: 126px;
    letter-spacing: 14px;
  }

  .worksite-scene {
    position: absolute;
    left: 0;
    bottom: 0;
    width: 1200px;
    height: 165px;
    background: linear-gradient(
      to bottom,
      rgba(255,255,255,1) 0%,
      #e6e8e6 30%,
      var(--haze) 72%,
      var(--haze) 86%,
      var(--ink) 90%,
      var(--ink) 100%
    );
  }
</style>
</head>
<body>
  <main class="billboard">
    <div class="flag-band" aria-hidden="true">
      <span class="blue"></span>
      <span class="yellow"></span>
      <span class="red"></span>
    </div>

    <h1 class="company-name">
      <span class="name-top">Vela</span>
      <span class="name-bottom">Structura</span>
    </h1>

    <div class="worksite-scene" role="img"
         aria-label="Silhouettes of road construction machinery, excavator, dump truck, rollers and workers in front of a faint city skyline with cranes"></div>
  </main>
</body>
</html>
```